THE REVEL OF GLIMBROOK Prospectus/Deck

We need a prospectus/deck made for this Halloween event called THE REVEL OF GLIMBROOK. Attached is the writeup, our logo, some background photos you can use, and photos of the actual town site. For the town photos (4) could you try to make them look greyscale or smokey? I attached a sample Prospectus/Deck that was created for another event of ours to give you an idea of layout and pages.

```html
<!DOCTYPE html>
<html lang="en">
<head>
<meta charset="utf-8">
<title>The Revel of Glimbrook – Prospectus</title>
<link rel="stylesheet" href="https://fonts.googleapis.com/css2?family=Creepster&family=Montserrat:wght@400;500;700;800&display=swap">
<style>
  :root {
    --board: #3d3d3d;
    --gold: #c8b15a;
    --leaf: #a3bf52;
    --ink-dark: #1b1e19;
    --white: #f2f2ee;
    --deep: #0e1a11;
    --fog: #c9d6c8;
    --band: #2f6b2a;
  }
  * { box-sizing: border-box; margin: 0; padding: 0; }
  html, body { width: 1146px; height: 1200px; overflow: hidden; background: var(--board); }
  body { position: relative; font-family: "Montserrat", sans-serif; color: var(--white); }

  .page { position: absolute; width: 503px; height: 350px; overflow: hidden; }
  .page-cover   { left: 57px;  top: 59px; }
  .page-intro   { left: 574px; top: 59px; }
  .page-about   { left: 57px;  top: 425px; }
  .page-vendor  { left: 574px; top: 425px; }
  .page-sponsor { left: 57px;  top: 790px; }
  .page-contact { left: 586px; top: 790px; }

  .photo { position: absolute; inset: 0; }
  .abs { position: absolute; }

  .brand-mark { position: absolute; width: 38px; text-align: center; }
  .brand-mark .dot { display: block; width: 30px; height: 30px; margin: 0 auto; border-radius: 50%; background: var(--gold); }
  .brand-mark .name { display: block; margin-top: 2px; font-size: 5px; font-weight: 700; letter-spacing: .3px; color: var(--gold); }

  .title { font-family: "Creepster", sans-serif; line-height: 1; letter-spacing: 1px; }
  .body-copy { font-size: 6.3px; line-height: 8px; }
  .label { font-size: 7px; font-weight: 500; letter-spacing: .2px; }
  .price { font-weight: 800; font-size: 16px; line-height: 18px; }
  ul.list { list-style: none; font-size: 6.2px; line-height: 7.9px; }
  ul.list li { position: relative; padding-left: 8px; }
  ul.list li::before { content: "·"; position: absolute; left: 0; }
  ul.ring li::before { content: "o"; font-size: 5px; }

  /* cover */
  .cover-kicker { left: 270px; top: 140px; font-size: 12px; font-weight: 700; letter-spacing: 4px; color: var(--gold); }
  .cover-name { left: 236px; top: 160px; font-size: 46px; color: var(--leaf); }
  .cover-tag { left: 262px; top: 246px; font-family: "Creepster", sans-serif; font-size: 13px; letter-spacing: .8px; color: var(--white); }
  .cover-date { left: 259px; top: 270px; padding: 1px 3px; background: var(--band); font-size: 9px; }
  .cover-line { left: 262px; font-size: 9px; }
</style>
</head>
<body>

<!-- Cover -->
<section class="page page-cover">
  <div class="photo" role="img" aria-label="Dark misty forest with a masked horned creature figure on the left"
       style="background: radial-gradient(ellipse at 28% 45%, #3d4a2c 0%, #1c2a1a 40%, #0a130c 100%);"></div>
  <div class="abs cover-kicker">THE REVEL OF</div>
  <div class="abs title cover-name">GLIMBROOK</div>
  <div class="abs cover-tag">Where terror meets Hollywood magic!</div>
  <div class="abs cover-date">October 6 – 31, 2023 (17 days)</div>
  <div class="abs cover-line" style="top:288px;">2150 Concession 9, Millbrook Ridge, Ontario K0L 2B0</div>
  <div class="abs cover-line" style="top:305px;">www.revelofglimbrook.ca</div>
</section>

<!-- Introduction -->
<section class="page page-intro">
  <div class="photo" role="img" aria-label="Smoky green-tinted aerial view of an empty main street in a film-set town"
       style="background: linear-gradient(180deg, #dfe7dc 0%, #c7d6c3 38%, #7f967c 55%, #4b5f4a 75%, #9fb39b 100%);"></div>
  <div class="brand-mark" style="left:9px; top:16px;"><span class="dot"></span><span class="name">GLIMBROOK</span></div>
  <div class="abs title" style="left:55px; top:28px; font-size:27px; color:var(--ink-dark);">INTRODUCTION</div>
  <p class="abs body-copy" style="left:54px; top:63px; width:432px; color:var(--ink-dark);">
    Welcome to The Revel of Glimbrook, where terror meets Hollywood magic! Step into our nightmare-inducing event set within a sprawling film studio lot at 2150 Concession 9, Millbrook Ridge, Ontario K0L 2B0 which has been transformed into a chillingly realistic little town. As you enter, you will find yourself immersed in the eerie atmosphere of a bygone era, where each corner holds lurking horrors. Our haunted experience offers a unique opportunity for vendors to become part of the terror by occupying the shops that line the Main Street of this sinister town. From creepy curiosities to spine-chilling treats, your store front will become a focal point of fear, allowing visitors to not only scream but also shop amidst the horrors. Prepare for a spine-tingling journey like no other as you explore our haunted event in this hauntingly realistic town. The Revel of Glimbrook is an exhilarating and spine-chilling haunted town experience that promises to deliver unforgettable thrills and scares. As we gear up for another terrifying season, we invite you to join us as a valued vendor or sponsor. This prospectus outlines the various opportunities available for your brand to be part of this highly anticipated event.
  </p>
</section>

<!-- About -->
<section class="page page-about">
  <div class="photo" role="img" aria-label="Misty overgrown garden with a ragged antlered scarecrow figure"
       style="background: linear-gradient(90deg, #9fb5a6 0%, #8ea794 30%, #4d6a3f 55%, #3a5530 80%, #6f8a62 100%);"></div>
  <div class="brand-mark" style="left:8px; top:26px;"><span class="dot"></span><span class="name">GLIMBROOK</span></div>
  <div class="abs title" style="left:52px; top:38px; font-size:24px; line-height:34px; color:var(--ink-dark);">About<br>The Revel<br>Of Glimbrook</div>
  <p class="abs body-copy" style="left:47px; top:151px; width:118px; color:var(--ink-dark);">
    The Revel of Glimbrook is a premier haunted town attraction known for its immersive and interactive experience that pushes the boundaries of fear. Our haunted town offers a meticulously designed setting with elaborate sets, talented actors, and cutting-edge special effects to create an atmosphere of horror and suspense. We attract a diverse audience of thrill-seekers, horror enthusiasts, families, and groups of friends, ensuring a wide reach for your brand.
  </p>
</section>

<!-- Vendor Opportunities -->
<section class="page page-vendor">
  <div class="photo" role="img" aria-label="Smoky dark interior with a bloodied costumed actor leaning on a counter"
       style="background: radial-gradient(ellipse at 78% 55%, #5a6a46 0%, #2c3a28 40%, #0f1710 100%);"></div>
  <div class="brand-mark" style="left:8px; top:24px;"><span class="dot"></span><span class="name">GLIMBROOK</span></div>
  <div class="abs title" style="left:47px; top:40px; font-size:22px; color:var(--gold);">VENDOR OPPORTUNITIES</div>

  <div class="abs label" style="left:53px; top:72px;">ON-SITE VENDORS:</div>
  <div class="abs" style="left:53px; top:86px; font-size:15px; line-height:17px;">Starting at</div>
  <div class="abs price" style="left:53px; top:103px;">$2500 + HST</div>
  <div class="abs" style="left:53px; top:123px; font-size:7px;">(per vendor; no sharing)</div>
  <p class="abs body-copy" style="left:53px; top:138px; width:114px;">
    depending on location and type of products/services sold and offered. Set up your booth within the haunted town premises and showcase your products or services to a captive audience in one of the existing buildings. Your brand will be exposed to thousands of visitors throughout the event. Examples of suitable vendors include:
  </p>
  <ul class="abs list ring" style="left:53px; top:227px; width:116px;">
    <li>Halloween costume shops</li>
    <li>Horror-themed merchandise</li>
    <li>Local/Artisan food vendors (pre-packaged items)</li>
    <li>Face painting and special effects makeup artists</li>
    <li>Paranormal investigators or ghost tour guides</li>
    <li>Novelty and souvenir vendors</li>
    <li>Psychic</li>
    <li>Metaphysical items and crystals</li>
  </ul>

  <div class="abs label" style="left:177px; top:72px;">FOOD TRUCKS</div>
  <div class="abs price" style="left:177px; top:90px;">$5000 + HST</div>
  <div class="abs" style="left:177px; top:110px; font-size:7px;">max of 3-4 total</div>
  <p class="abs body-copy" style="left:181px; top:138px; width:106px;">
    <b>Promotional Giveaways:</b> Partner with us to provide branded merchandise or samples to be distributed to our visitors. This opportunity allows you to directly engage with attendees and create lasting impressions of your brand.
  </p>
  <p class="abs body-copy" style="left:181px; top:203px; width:106px;">
    <b>Exclusive Sponsorship:</b> Become an exclusive sponsor of The Revel of Glimbrook. This comprehensive package offers maximum exposure and recognition for your brand. Benefits may include prominent logo placement, branding on event merchandise, on-site signage, social media promotions, and more. This option is ideal for businesses looking to establish a strong association with the haunted town and its audience.
  </p>
</section>

<!-- Sponsorship Tiers -->
<section class="page page-sponsor">
  <div class="photo" role="img" aria-label="Stormy green sky over a cornfield with graveyard crosses and a crow"
       style="background: linear-gradient(180deg, #1c2417 0%, #3c4a2c 45%, #6b7c3c 62%, #2a3a1c 80%, #141c10 100%);"></div>
  <div class="brand-mark" style="left:8px; top:16px;"><span class="dot"></span><span class="name">GLIMBROOK</span></div>
  <div class="abs title" style="left:57px; top:26px; font-size:24px; color:var(--white);">SPONSORSHIP TIERS</div>
  <p class="abs body-copy" style="left:56px; top:58px; width:410px;">
    We offer different sponsorship tiers to suit your marketing goals and budget. Please note that availability is limited for each tier, and commitments will be honored on a first-come, first-served basis. The sponsorship tiers include:
  </p>

  <div class="abs label" style="left:29px; top:89px; font-size:9px;">PLATINUM SPONSORSHIP:</div>
  <div class="abs price" style="left:29px; top:99px;">$15,000 + HST</div>
  <ul class="abs list" style="left:29px; top:118px; width:200px;">
    <li>Prominent logo placement on all marketing materials, including website, posters, flyers, and social media promotions</li>
    <li>Exclusive branding on event merchandise</li>
    <li>On-site signage and banners featuring your brand</li>
    <li>Dedicated social media posts highlighting your sponsorship</li>
    <li>Recognition during event announcements and media interviews</li>
    <li>Complimentary tickets for your staff or clients</li>
  </ul>

  <div class="abs label" style="left:236px; top:89px; font-size:9px;">GOLD SPONSORSHIP:</div>
  <div class="abs price" style="left:236px; top:99px;">$10,000 + HST</div>
  <ul class="abs list" style="left:236px; top:118px; width:120px;">
    <li>Logo placement on select marketing materials, including website, posters, and social media promotions</li>
    <li>On-site signage featuring your brand</li>
    <li>Social media mentions acknowledging your sponsorship</li>
    <li>Complimentary tickets for your staff or clients</li>
  </ul>

  <div class="abs label" style="left:364px; top:89px; font-size:9px;">SILVER SPONSORSHIP:</div>
  <div class="abs price" style="left:364px; top:99px;">$5,000 + HST</div>
  <ul class="abs list" style="left:364px; top:118px; width:126px;">
    <li>Logo placement on event website and select marketing materials</li>
    <li>On-site signage featuring your brand</li>
    <li>Complimentary tickets for your staff or clients</li>
  </ul>

  <p class="abs body-copy" style="left:26px; top:316px;">We are open to customizing sponsorship packages to meet your specific needs and objectives.</p>
</section>

<!-- Contact -->
<section class="page page-contact">
  <div class="photo" role="img" aria-label="Misty green forest with a hooded reaper figure holding a scythe"
       style="background: radial-gradient(ellipse at 45% 55%, #3e5a3c 0%, #26402a 45%, #0f1d13 100%);"></div>
  <div class="brand-mark" style="left:372px; top:20px;"><span class="dot"></span><span class="name">GLIMBROOK</span></div>
  <div class="abs title" style="left:300px; top:86px; width:188px; text-align:center; font-size:30px; color:var(--gold);">CONTACT US</div>
  <p class="abs" style="left:300px; top:136px; width:188px; text-align:center; font-size:8px; line-height:10px;">If you are interested in becoming<br>a vendor or sponsor for</p>
  <div class="abs" style="left:300px; top:167px; width:188px; text-align:center; font-size:6px; font-weight:700; letter-spacing:2.5px; color:var(--gold);">THE REVEL OF</div>
  <div class="abs title" style="left:300px; top:176px; width:188px; text-align:center; font-size:28px; color:var(--gold);">GLIMBROOK</div>
  <p class="abs" style="left:300px; top:223px; width:188px; text-align:center; font-size:7.5px;">please contact us at the following:</p>
  <p class="abs" style="left:300px; top:234px; width:188px; text-align:center; font-size:11px; font-weight:800;">mara@lanternevents.ca</p>
  <p class="abs body-copy" style="left:30px; top:244px; width:150px;">
    We would be delighted to discuss the available opportunities in more detail and tailor a package that aligns with your brand’s goals.<br><br>
    Do not miss the chance to be part of a frightfully fantastic experience that will haunt your customers’ memories for years to come. Join The Revel of Glimbrook as a vendor or sponsor and make this haunted town season one to remember!
  </p>
</section>

</body>
</html>
```